Copperleaf Injury

https://files.norvexa.com/doc/7QpLm2RtX9vKd4WzHs8NbYc3Fj6GaUe1/view?share=open

https://copperleafhealth.com/
https://bramblewick.com/
Please use photo and images from the websites and anything you need.

```html
<!DOCTYPE html>
<html lang="en">
<head>
<meta charset="utf-8">
<title>Copperleaf Injury Clinics – Flyer</title>
<link href="https://fonts.googleapis.com/css2?family=Montserrat:wght@300;400;500;700;800;900&family=Roboto:wght@400;500&display=swap" rel="stylesheet">
<style>
:root{
  --teal:#3dbca6;
  --teal-deep:#2fae98;
  --mint:#55d99a;
  --ink:#141414;
  --text:#2b2b2b;
  --paper:#ffffff;
  --canvas:#e6e7e7;
}
*{box-sizing:border-box;margin:0;padding:0}
html,body{width:690px;height:1200px;overflow:hidden;background:var(--canvas)}
body{position:relative;font-family:"Roboto",Arial,sans-serif;color:var(--text)}
.sheet{position:absolute;left:114px;width:615px;height:797px;background:var(--paper);transform:scale(.75);transform-origin:top left;overflow:hidden;box-shadow:0 4px 14px rgba(0,0,0,.12)}
.sheet--front{top:1px}
.sheet--back{top:601px}
.abs{position:absolute}
.header-art{position:absolute;left:0;top:0}
.brand{position:absolute;left:34px;top:52px;color:#fff;font-family:"Montserrat",sans-serif;font-weight:500;line-height:1}
.brand__dot{position:absolute;left:-2px;top:-10px;width:8px;height:8px;border-radius:50%;background:#fff}
.brand__name{font-size:30px;letter-spacing:1px;white-space:nowrap}
.brand__sub{font-size:13px;letter-spacing:2px;margin:6px 0 0 46px;white-space:nowrap}
.headline{position:absolute;left:30px;top:150px;font-family:"Montserrat",sans-serif;color:#fff;font-weight:400;line-height:1.05}
.headline__small{font-size:22px}
.headline__mid{font-size:30px}
.headline__big{font-size:82px;font-weight:900;color:var(--ink);letter-spacing:1px;margin-top:4px}
.headline__bar{width:60px;height:4px;background:var(--ink);margin-top:8px}
.intro{position:absolute;left:28px;top:340px;width:512px;font-size:8.4px;line-height:1.3;text-align:justify;color:#1e2a27}
.section-title{position:absolute;left:28px;font-family:"Montserrat",sans-serif;font-size:16px;font-weight:400;color:var(--ink)}
.section-title strong{font-weight:700}
.lead{position:absolute;left:30px;top:458px;width:470px;font-size:8.4px;line-height:1.3;color:#222}
.network{position:absolute;top:540px;width:260px;list-style:none}
.network--left{left:28px}
.network--right{left:330px}
.network li{display:flex;align-items:center;height:50px;font-size:8.4px;line-height:1.3;color:#222}
.network__icon{flex:none;width:34px;height:34px;border-radius:50%;background:var(--teal);margin-right:18px;position:relative}
.network__icon::after{content:"";position:absolute;inset:9px;border:2px solid #fff;border-radius:50%}
.network li:nth-child(even) .network__icon{background:var(--mint)}
.network__text{width:180px;text-align:justify}
.divider{position:absolute;background:#333;width:1px}
.footer{position:absolute;left:0;bottom:0;width:615px;height:66px}
.footer__phone{position:absolute;left:0;bottom:0;width:226px;height:54px;background:var(--ink);border-radius:0 30px 30px 0;display:flex;align-items:center;color:#fff}
.footer__phone-badge{width:30px;height:30px;border-radius:50%;background:#fff;margin:0 18px 0 14px;display:flex;align-items:center;justify-content:center}
.footer__phone-number{font-family:"Montserrat",sans-serif;font-size:19px;font-weight:400}
.footer__info{position:absolute;font-size:8px;line-height:1.5;color:#10302a;display:flex;gap:6px}
.footer__social{position:absolute;left:520px;top:30px;width:44px;height:12px;border-radius:6px;background:var(--ink)}
.footer__rule{position:absolute;left:560px;top:35px;width:55px;height:1.5px;background:var(--ink)}
.timeline{position:absolute;list-style:none}
.timeline::before{content:"";position:absolute;left:3px;top:4px;bottom:14px;width:1px;background:#bbb}
.timeline li{position:relative;padding-left:20px;font-size:8.2px;line-height:1.35;color:#222;text-align:justify}
.timeline li::before{content:"";position:absolute;left:0;top:3px;width:7px;height:7px;border-radius:50%;background:var(--teal)}
.partner-name{position:absolute;left:372px;top:680px;font-family:"Montserrat",sans-serif;font-weight:900;font-size:26px;color:var(--ink);letter-spacing:.5px}
</style>
</head>
<body>

<section class="sheet sheet--front">
  <svg class="header-art" width="615" height="420" viewBox="0 0 615 420">
    <defs>
      <linearGradient id="panelFront" x1="0" y1="0" x2="1" y2="1">
        <stop offset="0" stop-color="#3dbca6"/><stop offset="1" stop-color="#55d99a"/>
      </linearGradient>
      <linearGradient id="doctorsFill" x1="0" y1="0" x2="1" y2="1">
        <stop offset="0" stop-color="#e9ecee"/><stop offset=".6" stop-color="#cdd6da"/><stop offset="1" stop-color="#b9c4c8"/>
      </linearGradient>
    </defs>
    <path d="M0 0H615V370Q615 410 575 410H0Z" fill="url(#panelFront)"/>
    <circle cx="468" cy="158" r="172" fill="#fff"/>
    <circle cx="612" cy="165" r="58" fill="#3dbca6"/>
    <path d="M592 103 A136 136 0 1 0 592 213" fill="none" stroke="#3dbca6" stroke-width="26"/>
    <circle cx="468" cy="158" r="104" fill="url(#doctorsFill)" role="img" aria-label="Photo of two smiling female doctors in white coats"/>
  </svg>

  <div class="brand">
    <span class="brand__dot"></span>
    <div class="brand__name">COPPERLEAF</div>
    <div class="brand__sub">INJURY CLINICS</div>
  </div>

  <div class="headline">
    <div class="headline__small">PERSONAL INJURY &amp;</div>
    <div class="headline__mid">CAR ACCIDENT</div>
    <div class="headline__big">CARE</div>
    <div class="headline__bar"></div>
  </div>

  <p class="intro">Atlanta Area, at Copperleaf Injury Clinics, we believe that the best care for our patients occurs when a patient is treated by chiropractors, physical therapists and medical treatment physicians. Our medical professionals include Atlanta's top personal injury chiropractors, neurosurgeons, interventional pain physicians, orthopedic extremity physicians, neurologists and physical therapists. They take the time to diagnose and treat the injuries caused by their motor vehicle accident, slip and fall or premise liability injury, which allows our patients to achieve maximum medical improvement and recovery from their injuries.</p>

  <h2 class="section-title" style="top:424px">ZERO OUT OF POCKET COST TO <strong>OUR PATIENTS</strong></h2>
  <p class="lead">Our top priority is our patients' health! At Copperleaf Health and all Copperleaf affiliate locations, we work with your attorney, Med Pay Insurance, and/or personal health insurance to ensure that you receive the highest level of care for the injuries that you sustained from your accident.</p>

  <h2 class="section-title" style="top:504px">THE NETWORK</h2>
  <ul class="network network--left">
    <li><span class="network__icon"></span><span class="network__text">Over 30 Chiropractic Locations Across Georgia and growing daily</span></li>
    <li><span class="network__icon"></span><span class="network__text">Over 20 Physical Therapy Locations Across Georgia</span></li>
    <li><span class="network__icon"></span><span class="network__text">Referral Network with Neurosurgery, Orthopedic and Interventional Spine Clinics</span></li>
    <li><span class="network__icon"></span><span class="network__text">Co Treat with Medical Doctors</span></li>
  </ul>
  <div class="divider" style="left:298px;top:545px;height:165px"></div>
  <ul class="network network--right">
    <li><span class="network__icon"></span><span class="network__text">Manage the Imaging Process</span></li>
    <li><span class="network__icon"></span><span class="network__text">Team of 40 Case Managers to insure your clients are getting the best care possible</span></li>
    <li><span class="network__icon"></span><span class="network__text">Multilingual Staff</span></li>
    <li><span class="network__icon"></span><span class="network__text">Transportation Provided</span></li>
  </ul>

  <footer class="footer">
    <svg class="abs" style="left:0;top:0" width="615" height="66" viewBox="0 0 615 66"><path d="M70 16Q72 0 90 0H615V66H70Z" fill="#3dbca6"/></svg>
    <div class="footer__phone">
      <span class="footer__phone-badge"><svg width="16" height="16" viewBox="0 0 24 24"><path d="M6.6 10.8a15 15 0 0 0 6.6 6.6l2.2-2.2c.3-.3.7-.4 1-.2 1.1.4 2.3.6 3.6.6.6 0 1 .4 1 1V20c0 .6-.4 1-1 1A17 17 0 0 1 3 4c0-.6.4-1 1-1h3.5c.6 0 1 .4 1 1 0 1.3.2 2.5.6 3.6.1.3 0 .7-.2 1z" fill="#141414"/></svg></span>
      <span class="footer__phone-number">(555) 014-2200</span>
    </div>
    <div class="footer__info" style="left:248px;top:22px"><svg width="8" height="10" viewBox="0 0 8 10"><path d="M4 0a3 3 0 0 1 3 3c0 2.3-3 6-3 6S1 5.3 1 3a3 3 0 0 1 3-3z" fill="none" stroke="#10302a"/></svg><span>Ashford. Glenmoor.<br>Redvale. Pinecrest.</span></div>
    <div class="footer__info" style="left:375px;top:18px"><svg width="8" height="24" viewBox="0 0 8 24"><circle cx="4" cy="5" r="3.2" fill="none" stroke="#10302a"/><rect x="0.5" y="16" width="7" height="5" fill="none" stroke="#10302a"/></svg><span>copperleafhealth.com<br>info@copperleafhealth.com</span></div>
    <div class="footer__social"></div><div class="footer__rule"></div>
  </footer>
</section>

<section class="sheet sheet--back">
  <svg class="header-art" width="615" height="420" viewBox="0 0 615 420">
    <defs>
      <linearGradient id="panelBack" x1="0" y1="0" x2="1" y2="1">
        <stop offset="0" stop-color="#3dbca6"/><stop offset="1" stop-color="#55d99a"/>
      </linearGradient>
      <linearGradient id="checkFill" x1="0" y1="0" x2="1" y2="1">
        <stop offset="0" stop-color="#5d7c7c"/><stop offset="1" stop-color="#3a5556"/>
      </linearGradient>
    </defs>
    <path d="M0 0H615V370Q615 410 575 410H0Z" fill="url(#panelBack)"/>
    <circle cx="468" cy="158" r="172" fill="#fff"/>
    <circle cx="612" cy="165" r="58" fill="#3dbca6"/>
    <path d="M592 103 A136 136 0 1 0 592 213" fill="none" stroke="#3dbca6" stroke-width="26"/>
    <circle cx="468" cy="158" r="104" fill="url(#checkFill)" role="img" aria-label="Photo of a clinician measuring a patient's blood pressure beside a stethoscope"/>
    <rect x="20" y="150" width="270" height="260" fill="#3fb79f" opacity=".55" role="img" aria-label="Photo of a smiling man in glasses holding a white mug"/>
  </svg>

  <div class="brand" style="top:72px">
    <span class="brand__dot"></span>
    <div class="brand__name">COPPERLEAF</div>
    <div class="brand__sub">INJURY CLINICS</div>
  </div>

  <ul class="timeline" style="left:50px;top:432px;width:226px">
    <li style="margin-bottom:24px">Powered by AI</li>
    <li style="margin-bottom:18px">HIPPA Compliant Case Management Software - Our site is HIPAA compliant and all information is secured using the most advanced technology available.</li>
    <li style="margin-bottom:18px">Award-Winning Analytics - Analyzes data from thousands of cases and uses artificial intelligence to recommend action items that will increase the settlement amount. We have the most powerful analytics in the game. Period.</li>
    <li style="margin-bottom:14px">Document Management Simplified - We're taking the headache out of managing medical records and bills. Share documents with other lien holders securely and instantly.</li>
    <li>Cloud-Based - Access Bramblewick from any device you choose. When you're on-the-go, you need quick access to case information – we securely store your data so you can access it anywhere, anytime.</li>
  </ul>
  <div class="divider" style="left:307px;top:440px;height:290px;background:#bbb"></div>
  <ul class="timeline" style="left:354px;top:438px;width:228px">
    <li style="margin-bottom:18px">AI to track any gaps in treatment - Bramblewick delivers important updates about your case, so that every stakeholder has the information they need to operate in their respective area of the case.</li>
    <li style="margin-bottom:22px">Centralized Scheduling</li>
    <li style="margin-bottom:14px">Centralized Notes and Records</li>
    <li style="margin-bottom:24px">Centralized Reductions</li>
    <li>Round-the-Clock Support</li>
  </ul>
  <div class="partner-name">BRAMBLEWICK</div>

  <footer class="footer">
    <svg class="abs" style="left:0;top:0" width="615" height="66" viewBox="0 0 615 66"><path d="M70 16Q72 0 90 0H615V66H70Z" fill="#3dbca6"/></svg>
    <div class="footer__phone">
      <span class="footer__phone-badge"><svg width="16" height="16" viewBox="0 0 24 24"><path d="M6.6 10.8a15 15 0 0 0 6.6 6.6l2.2-2.2c.3-.3.7-.4 1-.2 1.1.4 2.3.6 3.6.6.6 0 1 .4 1 1V20c0 .6-.4 1-1 1A17 17 0 0 1 3 4c0-.6.4-1 1-1h3.5c.6 0 1 .4 1 1 0 1.3.2 2.5.6 3.6.1.3 0 .7-.2 1z" fill="#141414"/></svg></span>
      <span class="footer__phone-number">(555) 014-2200</span>
    </div>
    <div class="footer__info" style="left:248px;top:22px"><svg width="8" height="10" viewBox="0 0 8 10"><path d="M4 0a3 3 0 0 1 3 3c0 2.3-3 6-3 6S1 5.3 1 3a3 3 0 0 1 3-3z" fill="none" stroke="#10302a"/></svg><span>Ashford. Glenmoor.<br>Redvale. Pinecrest.</span></div>
    <div class="footer__info" style="left:375px;top:18px"><svg width="8" height="24" viewBox="0 0 8 24"><circle cx="4" cy="5" r="3.2" fill="none" stroke="#10302a"/><rect x="0.5" y="16" width="7" height="5" fill="none" stroke="#10302a"/></svg><span>copperleafhealth.com<br>info@copperleafhealth.com</span></div>
    <div class="footer__social"></div><div class="footer__rule"></div>
  </footer>
</section>

</body>
</html>
```